Bref créative
Business Card for Education Consulting Company
Brio Study Mentors
Simple
Marcus Delavine
President
317 Hollins Court NE
Washington DC 20019
Marcus@briostudymentors-example.com
www.briostudymentors-example.com
Looking for a simple, clean and professional business card. The logo already has the name of the company so there is no need to include again unless you feel it adds to the overall look of the card.
Here is the compnay's logo

```html
<!DOCTYPE html>
<html lang="en">
<head>
<meta charset="utf-8">
<title>Brio Study Mentors – Stationery</title>
<link href="https://fonts.googleapis.com/css2?family=Open+Sans:wght@400;600;700&display=swap" rel="stylesheet">
<style>
  :root{
    --bg-light:#b9b9b9;
    --bg-dark:#8f8f8f;
    --paper:#ffffff;
    --brand-blue:#1f5fbf;
    --brand-navy:#1b3f7a;
    --swoosh-grey:#8a8f96;
    --text-grey:#6d737a;
    --faint:#eef1f5;
    --flap:#7f858c;
  }
  *{box-sizing:border-box;margin:0;padding:0}
  html,body{width:1200px;height:479px;overflow:hidden}
  body{
    font-family:"Open Sans",Arial,sans-serif;
    background:radial-gradient(ellipse at 55% 40%,var(--bg-light),var(--bg-dark));
    position:relative;
  }
  .piece{position:absolute;background:var(--paper);box-shadow:0 2px 6px rgba(0,0,0,.25);overflow:hidden}
  .brand{display:flex;align-items:center;gap:3px;color:var(--brand-navy);font-weight:700;white-space:nowrap}
  .brand .dot{width:.9em;height:.9em;border-radius:50%;background:var(--brand-blue);flex:none}
  .swoosh{position:absolute;left:0;bottom:0;width:100%}
  .tiny{font-size:4px;color:var(--text-grey);line-height:1.5}
  .faint-circle{position:absolute;border-radius:50%;background:var(--faint)}
  .footer-url{position:absolute;bottom:4px;width:100%;text-align:center;font-size:4px;color:#fff}

  /* business cards */
  .card{width:80px;height:74px}
  .card-front{left:36px;top:149px}
  .card-back{left:36px;top:235px}
  .card-front .brand{position:absolute;left:6px;top:22px;font-size:6px}
  .card-front .contact{position:absolute;left:40px;top:14px}
  .card-front .name{font-size:4.5px;font-weight:600;color:var(--brand-navy)}
  .card-back .brand{position:absolute;left:50%;top:26px;transform:translateX(-50%);font-size:7px}

  /* letterhead & fax */
  .sheet{width:286px;height:405px;top:29px}
  .letterhead{left:194px}
  .fax{left:516px}
  .sheet .brand{position:absolute;left:14px;top:14px;font-size:10px}
  .sheet .address{position:absolute;right:16px;top:14px;text-align:left}
  .sheet .faint-circle{width:96px;height:96px;left:95px;top:150px}
  .fax-title{position:absolute;left:14px;top:62px;font-size:9px;font-weight:700;color:#333}
  .fax-fields{position:absolute;left:14px;top:80px;width:258px;display:grid;grid-template-columns:1fr 1fr;column-gap:12px;row-gap:5px}
  .fax-fields div{font-size:4px;color:#444;border-bottom:.5px solid #aaa;padding-bottom:1px}
  .fax-checks{position:absolute;left:14px;top:128px;width:258px;display:flex;justify-content:space-between;font-size:4px;color:#444}
  .fax-checks span::before{content:"";display:inline-block;width:4px;height:4px;border:.5px solid #666;margin-right:2px;vertical-align:middle}
  .fax-comments{position:absolute;left:14px;top:148px;font-size:4px;color:#444}

  /* envelopes */
  .envelope{width:336px}
  .env-front{left:828px;top:29px;height:168px}
  .env-front .brand{position:absolute;left:14px;top:12px;font-size:9px}
  .env-front .address{position:absolute;right:16px;top:12px}
  .env-front .faint-circle{width:50px;height:50px;right:30px;top:36px}
  .env-back{left:828px;top:252px;height:84px;background:var(--flap)}
  .env-back .brand{position:absolute;left:50%;top:38px;transform:translateX(-50%);font-size:9px;color:#fff}
  .env-back .brand .dot{background:#fff}
  .env-open{left:828px;top:312px;height:120px}
  .env-open .brand{position:absolute;left:50%;top:56px;transform:translateX(-50%);font-size:9px}
</style>
</head>
<body>

  <!-- business card front -->
  <section class="piece card card-front">
    <div class="brand"><span class="dot"></span>Brio</div>
    <div class="contact">
      <p class="name">Marcus Delavine</p>
      <p class="tiny">President</p>
      <p class="tiny">317 Hollins Court NE</p>
      <p class="tiny">Washington DC 20019</p>
      <p class="tiny">(202) 555-0147</p>
    </div>
    <svg class="swoosh" viewBox="0 0 80 18" preserveAspectRatio="none" height="18">
      <path d="M0 6 Q40 -2 80 4 L80 18 L0 18Z" fill="var(--swoosh-grey)"/>
      <path d="M0 9 Q40 2 80 7 L80 18 L0 18Z" fill="var(--brand-blue)"/>
    </svg>
  </section>

  <!-- business card back -->
  <section class="piece card card-back">
    <div class="faint-circle" style="width:40px;height:40px;left:36px;top:8px"></div>
    <div class="brand"><span class="dot"></span>Brio Study Mentors</div>
    <svg class="swoosh" viewBox="0 0 80 18" preserveAspectRatio="none" height="18">
      <path d="M0 6 Q40 -2 80 4 L80 18 L0 18Z" fill="var(--swoosh-grey)"/>
      <path d="M0 9 Q40 2 80 7 L80 18 L0 18Z" fill="var(--brand-blue)"/>
    </svg>
  </section>

  <!-- letterhead -->
  <section class="piece sheet letterhead">
    <div class="brand"><span class="dot"></span>Brio Study Mentors</div>
    <div class="address">
      <p class="tiny">317 Hollins Court NE</p>
      <p class="tiny">Washington DC 20019</p>
      <p class="tiny">(202) 555-0147</p>
    </div>
    <div class="faint-circle"></div>
    <svg class="swoosh" viewBox="0 0 286 40" preserveAspectRatio="none" height="40">
      <path d="M0 14 Q143 -4 286 10 L286 40 L0 40Z" fill="var(--swoosh-grey)"/>
      <path d="M0 19 Q143 2 286 15 L286 40 L0 40Z" fill="var(--brand-blue)"/>
    </svg>
    <p class="footer-url">www.briostudymentors-example.com</p>
  </section>

  <!-- fax sheet -->
  <section class="piece sheet fax">
    <div class="brand"><span class="dot"></span>Brio Study Mentors</div>
    <div class="address">
      <p class="tiny">317 Hollins Court NE</p>
      <p class="tiny">Washington DC 20019</p>
      <p class="tiny">(202) 555-0147</p>
    </div>
    <h1 class="fax-title">FAX</h1>
    <div class="fax-fields">
      <div>To:</div><div>From:</div>
      <div>Fax:</div><div>Pages:</div>
      <div>Phone:</div><div>Date:</div>
      <div>Re:</div><div>CC:</div>
    </div>
    <div class="fax-checks">
      <span>Urgent</span><span>For Review</span><span>Please Comment</span><span>Please Reply</span><span>Please Recycle</span>
    </div>
    <p class="fax-comments">Comments:</p>
    <div class="faint-circle"></div>
    <svg class="swoosh" viewBox="0 0 286 40" preserveAspectRatio="none" height="40">
      <path d="M0 14 Q143 -4 286 10 L286 40 L0 40Z" fill="var(--swoosh-grey)"/>
      <path d="M0 19 Q143 2 286 15 L286 40 L0 40Z" fill="var(--brand-blue)"/>
    </svg>
    <p class="footer-url">www.briostudymentors-example.com</p>
  </section>

  <!-- envelope front -->
  <section class="piece envelope env-front">
    <div class="brand"><span class="dot"></span>Brio Study Mentors</div>
    <div class="address">
      <p class="tiny">317 Hollins Court NE, Washington DC 20019</p>
    </div>
    <div class="faint-circle"></div>
    <svg class="swoosh" viewBox="0 0 336 80" preserveAspectRatio="none" height="80">
      <path d="M0 14 Q168 -6 336 10 L336 30 Q168 12 0 32Z" fill="var(--swoosh-grey)"/>
      <path d="M0 22 Q168 4 336 18 L336 36 Q168 22 0 40Z" fill="var(--brand-blue)"/>
    </svg>
  </section>

  <!-- envelope back with flap -->
  <section class="piece envelope env-back">
    <svg class="swoosh" viewBox="0 0 336 84" preserveAspectRatio="none" height="84" style="top:0">
      <path d="M0 0 L336 0 L336 20 Q168 70 0 20Z" fill="#9aa0a6"/>
    </svg>
    <div class="brand"><span class="dot"></span>Brio</div>
  </section>

  <!-- envelope with open flap -->
  <section class="piece envelope env-open">
    <svg class="swoosh" viewBox="0 0 336 60" preserveAspectRatio="none" height="60" style="top:0">
      <path d="M0 0 L336 0 L168 46Z" fill="#e4e6e9"/>
    </svg>
    <div class="brand"><span class="dot"></span>Brio</div>
  </section>

</body>
</html>
```